Tumble Tail (Pet Supplies) Home Page

For our Tumble Tail website, we want this to be fun and playful but with a touch of your creativity! Tumble Tail is a fun-loving brand that sells pet supplies and accessories focused on accentuating the love between pets and their owners. We want to advertise these products in a welcoming way, making the customer receive the happiness the brand offers.

Target Market(s)

Main demo: Female pet owners online shopping 18-34. Secondary demo: All pet owners online shopping 18-34.

Number of Pages Required

1 page

```html
<!DOCTYPE html>
<html lang="en">
<head>
<meta charset="utf-8">
<title>Tumble Tail – Home</title>
<link href="https://fonts.googleapis.com/css2?family=Fredoka:wght@400;500;600&display=swap" rel="stylesheet">
<style>
:root{
  --teal:#3ec6c8;
  --teal-dark:#27a9ad;
  --purple:#8f45a8;
  --purple-dark:#74358a;
  --pink:#e9457d;
  --pink-soft:#fbe1e6;
  --orange:#f28a3d;
  --ink:#3b3340;
  --muted:#8a8290;
  --line:#e6e1ea;
  --white:#ffffff;
}
*{box-sizing:border-box;margin:0;padding:0}
html,body{width:1200px;height:2404px;overflow:hidden}
body{font-family:"Fredoka",sans-serif;color:var(--ink);background:var(--white);position:relative}
a{color:inherit;text-decoration:none}

/* header */
.site-header{position:absolute;top:0;left:0;width:1200px;height:72px;background:var(--white)}
.brand{position:absolute;left:12px;top:0;width:164px;height:72px;background:var(--teal);display:flex;align-items:center;justify-content:center;gap:8px;color:var(--white);font-size:17px;font-weight:600}
.brand-dot{width:18px;height:18px;border-radius:50%;background:var(--white)}
.main-nav{position:absolute;left:420px;top:26px;display:flex;gap:62px;font-size:15px;color:var(--purple);font-weight:500}
.header-icons{position:absolute;right:20px;top:22px;display:flex;gap:22px;align-items:center}
.header-icons svg{width:24px;height:24px}
.promo-bar{position:absolute;top:72px;left:0;width:1200px;height:24px;background:var(--pink-soft);text-align:center;font-size:11px;line-height:24px;color:var(--pink)}

/* hero */
.hero{position:absolute;top:96px;left:0;width:1200px;height:496px}
.hero-photo{position:absolute;inset:0;background:linear-gradient(100deg,#c9d6c4 0%,#eef1ea 40%,#f4efe6 60%,#a8b89a 100%)}
.hero-copy{position:absolute;left:112px;top:188px;font-size:30px;line-height:36px;color:var(--white);font-weight:500;text-shadow:0 1px 3px rgba(0,0,0,.25)}
.hero-copy em{font-style:normal;color:var(--teal)}
.hero-cta{position:absolute;left:112px;top:282px;width:104px;height:32px;border-radius:4px;background:var(--orange);color:var(--white);font-size:14px;line-height:32px;text-align:center}
.hero-arrow{position:absolute;top:230px;width:24px;height:36px}
.hero-arrow.prev{left:18px}.hero-arrow.next{right:18px}

/* products */
.section-title{font-size:22px;font-weight:500;color:var(--purple)}
.favorites-head{position:absolute;top:672px;left:228px;width:744px;display:flex;justify-content:space-between;align-items:baseline}
.view-all{font-size:13px;color:var(--ink)}
.product-grid{position:absolute;top:740px;left:228px;display:grid;grid-template-columns:repeat(4,172px);gap:16px 16px}
.product-card{height:292px;border-radius:8px;border:1px solid var(--line);background:var(--white);box-shadow:0 2px 8px rgba(0,0,0,.08);overflow:hidden;position:relative}
.product-photo{height:166px;background:linear-gradient(160deg,#f06a95,#e0336e)}
.product-meta{display:flex;justify-content:space-between;padding:10px 10px 0;font-size:12px;color:var(--purple)}
.product-price{color:var(--ink)}
.swatches{display:flex;gap:5px;padding:10px 10px 0}
.swatches i{width:12px;height:12px;border-radius:2px;display:block}
.sale-tag{font-size:10px;color:var(--muted);padding:6px 10px 0;text-align:center}
.add-cart{position:absolute;left:10px;bottom:12px;width:80px;height:22px;border-radius:3px;background:var(--orange);color:var(--white);font-size:10px;line-height:22px;text-align:center}

/* partners */
.partner-band{position:absolute;top:1432px;left:0;width:1200px;height:140px;background:linear-gradient(90deg,var(--teal-dark),var(--teal) 60%,#5fd7cf)}
.partner-copy{position:absolute;left:228px;top:28px;font-size:15px;color:var(--white)}
.partner-copy b{color:#fff27a;font-weight:500}
.partner-names{position:absolute;left:228px;top:68px;display:flex;gap:60px;align-items:center;color:var(--white);font-size:34px;font-weight:600}
.partner-names .sm{font-size:26px;display:flex;align-items:center;gap:10px}
.partner-names .sm i{width:22px;height:22px;border-radius:50%;background:var(--white);display:block}

/* testimonials */
.testimonials{position:absolute;top:1572px;left:0;width:1200px;height:540px;background:linear-gradient(180deg,#f7ede3,#fbf5ef 40%,#fdfaf6)}
.testimonials .section-title{position:absolute;top:94px;left:0;width:1200px;text-align:center}
.quote-card{position:absolute;top:148px;left:228px;width:748px;height:192px;background:var(--white);border-radius:8px;box-shadow:0 3px 12px rgba(0,0,0,.12);overflow:hidden}
.quote-photo{position:absolute;left:0;top:0;width:312px;height:192px;background:linear-gradient(135deg,#cfe3e0,#b89a74)}
.quote-text{position:absolute;left:344px;top:28px;width:372px;font-size:15px;line-height:24px;color:var(--ink)}
.quote-author{position:absolute;right:34px;bottom:24px;font-size:13px;color:var(--purple);font-weight:500}
.thumbs{position:absolute;top:380px;left:292px;display:flex;gap:110px}
.thumb{width:68px;height:68px;border-radius:6px;background:linear-gradient(135deg,#e8ddd0,#c4b096);border:2px solid var(--white);box-shadow:0 2px 6px rgba(0,0,0,.12)}
.rewards-pill{position:absolute;top:2064px;left:16px;width:160px;height:34px;border-radius:17px;background:var(--teal);color:var(--white);font-size:12px;display:flex;align-items:center;gap:8px;padding-left:12px}
.rewards-pill i{width:16px;height:16px;border-radius:50%;background:var(--white);display:block}
.chat-btn{position:absolute;top:2052px;right:16px;width:44px;height:44px;border-radius:50%;background:var(--teal)}

/* footer */
.site-footer{position:absolute;top:2112px;left:0;width:1200px;height:252px;background:var(--purple);color:var(--white)}
.footer-brand{position:absolute;left:248px;top:34px;display:flex;align-items:center;gap:8px;font-size:15px;font-weight:600}
.footer-brand i{width:16px;height:16px;border-radius:50%;background:var(--white);display:block}
.social{position:absolute;left:248px;top:78px;display:flex;gap:14px}
.social i{width:16px;height:16px;border-radius:50%;background:var(--white);display:block;opacity:.9}
.contact{position:absolute;left:248px;top:112px;font-size:11px;line-height:22px;list-style:none}
.footer-col{position:absolute;top:32px;font-size:11px;line-height:20px;list-style:none}
.footer-col h4{font-size:12px;font-weight:500;letter-spacing:.5px;margin-bottom:8px}
.col-company{left:384px}.col-help{left:548px}
.newsletter{position:absolute;left:708px;top:32px;width:260px}
.newsletter h4{font-size:12px;font-weight:500;letter-spacing:.5px;margin-bottom:8px}
.newsletter p{font-size:10px;line-height:16px;opacity:.9}
.news-form{display:flex;margin-top:10px}
.news-form span{flex:1;height:24px;background:var(--white);border-radius:3px 0 0 3px;color:var(--muted);font-size:10px;line-height:24px;padding-left:8px}
.news-form b{width:62px;height:24px;background:var(--teal);border-radius:0 3px 3px 0;font-size:10px;font-weight:500;line-height:24px;text-align:center}
.footer-bottom{position:absolute;top:2364px;left:0;width:1200px;height:40px;background:var(--purple-dark);color:var(--white);font-size:10px;line-height:40px;padding-left:248px;opacity:.95}
</style>
</head>
<body>

<header class="site-header">
  <a class="brand"><i class="brand-dot"></i>Tumble Tail</a>
  <nav class="main-nav"><a>Shop</a><a>Our Story</a><a>Blog Plus</a><a>Pet Beauty Kit</a></nav>
  <div class="header-icons">
    <svg viewBox="0 0 24 24" fill="none" stroke="#8f45a8" stroke-width="2"><circle cx="10" cy="10" r="7"/><path d="M15 15l6 6"/></svg>
    <svg viewBox="0 0 24 24" fill="none" stroke="#e9457d" stroke-width="2"><circle cx="12" cy="8" r="4"/><path d="M4 21c1-5 5-7 8-7s7 2 8 7"/></svg>
    <svg viewBox="0 0 24 24" fill="none" stroke="#3b3340" stroke-width="2"><path d="M3 4h3l2 11h11l2-8H7"/><circle cx="9" cy="20" r="1.5"/><circle cx="18" cy="20" r="1.5"/></svg>
  </div>
</header>
<div class="promo-bar">Free shipping on every order over $50 this week</div>

<section class="hero">
  <div class="hero-photo" role="img" aria-label="Photo of a happy puppy playing with a colourful toy on green grass"></div>
  <h1 class="hero-copy">Because your pet family<br>deserves the <em>best love</em></h1>
  <a class="hero-cta">Shop Now</a>
  <svg class="hero-arrow prev" viewBox="0 0 24 36" fill="none" stroke="#fff" stroke-width="3"><path d="M18 4L6 18l12 14"/></svg>
  <svg class="hero-arrow next" viewBox="0 0 24 36" fill="none" stroke="#fff" stroke-width="3"><path d="M6 4l12 14L6 32"/></svg>
</section>

<div class="favorites-head"><h2 class="section-title">Furry Favorites</h2><a class="view-all">View All</a></div>
<section class="product-grid">
  <article class="product-card"><div class="product-photo" role="img" aria-label="Product photo of a small dog with a toy on pink"></div><div class="product-meta"><span>Lorem Ipsum</span><span class="product-price">$50</span></div><div class="swatches"><i style="background:#f4a9b8"></i><i style="background:#f28a3d"></i><i style="background:#8f45a8"></i><i style="background:#3ec6c8"></i><i style="background:#6fbf73"></i></div><p class="sale-tag">Sale</p><a class="add-cart">Add to Cart</a></article>
  <article class="product-card"><div class="product-photo" role="img" aria-label="Product photo of a small dog with a toy on pink"></div><div class="product-meta"><span>Lorem Ipsum</span><span class="product-price">$50</span></div><div class="swatches"><i style="background:#f4a9b8"></i><i style="background:#f28a3d"></i><i style="background:#8f45a8"></i><i style="background:#3ec6c8"></i><i style="background:#6fbf73"></i></div><p class="sale-tag">Sale</p><a class="add-cart">Add to Cart</a></article>
  <article class="product-card"><div class="product-photo" role="img" aria-label="Product photo of a small dog with a toy on pink"></div><div class="product-meta"><span>Lorem Ipsum</span><span class="product-price">$50</span></div><div class="swatches"><i style="background:#f4a9b8"></i><i style="background:#f28a3d"></i><i style="background:#8f45a8"></i><i style="background:#3ec6c8"></i><i style="background:#6fbf73"></i></div><p class="sale-tag">Sale</p><a class="add-cart">Add to Cart</a></article>
  <article class="product-card"><div class="product-photo" role="img" aria-label="Product photo of a small dog with a toy on pink"></div><div class="product-meta"><span>Lorem Ipsum</span><span class="product-price">$50</span></div><div class="swatches"><i style="background:#f4a9b8"></i><i style="background:#f28a3d"></i><i style="background:#8f45a8"></i><i style="background:#3ec6c8"></i><i style="background:#6fbf73"></i></div><p class="sale-tag">Sale</p><a class="add-cart">Add to Cart</a></article>
  <article class="product-card"><div class="product-photo" role="img" aria-label="Product photo of a small dog with a toy on pink"></div><div class="product-meta"><span>Lorem Ipsum</span><span class="product-price">$50</span></div><div class="swatches"><i style="background:#f4a9b8"></i><i style="background:#f28a3d"></i><i style="background:#8f45a8"></i><i style="background:#3ec6c8"></i><i style="background:#6fbf73"></i></div><p class="sale-tag">Sale</p><a class="add-cart">Add to Cart</a></article>
  <article class="product-card"><div class="product-photo" role="img" aria-label="Product photo of a small dog with a toy on pink"></div><div class="product-meta"><span>Lorem Ipsum</span><span class="product-price">$50</span></div><div class="swatches"><i style="background:#f4a9b8"></i><i style="background:#f28a3d"></i><i style="background:#8f45a8"></i><i style="background:#3ec6c8"></i><i style="background:#6fbf73"></i></div><p class="sale-tag">Sale</p><a class="add-cart">Add to Cart</a></article>
  <article class="product-card"><div class="product-photo" role="img" aria-label="Product photo of a small dog with a toy on pink"></div><div class="product-meta"><span>Lorem Ipsum</span><span class="product-price">$50</span></div><div class="swatches"><i style="background:#f4a9b8"></i><i style="background:#f28a3d"></i><i style="background:#8f45a8"></i><i style="background:#3ec6c8"></i><i style="background:#6fbf73"></i></div><p class="sale-tag">Sale</p><a class="add-cart">Add to Cart</a></article>
  <article class="product-card"><div class="product-photo" role="img" aria-label="Product photo of a small dog with a toy on pink"></div><div class="product-meta"><span>Lorem Ipsum</span><span class="product-price">$50</span></div><div class="swatches"><i style="background:#f4a9b8"></i><i style="background:#f28a3d"></i><i style="background:#8f45a8"></i><i style="background:#3ec6c8"></i><i style="background:#6fbf73"></i></div><p class="sale-tag">Sale</p><a class="add-cart">Add to Cart</a></article>
</section>

<section class="partner-band">
  <p class="partner-copy">Buy your furry family their gifts <b>Today</b> and pay <b>Later</b> with our partners</p>
  <div class="partner-names"><span>Paysoon</span><span class="sm"><i></i>Loafly</span></div>
</section>

<section class="testimonials">
  <h2 class="section-title">What our Furry Friends say about us</h2>
  <div class="quote-card">
    <div class="quote-photo" role="img" aria-label="Photo of a small dog standing on a sandy path"></div>
    <p class="quote-text">Before Tumble Tail my human bought me gifts that made me want to dig a hole under the fence and run. Now I still dig, but it's to bury all my awesome toys!</p>
    <span class="quote-author">— BELLA</span>
  </div>
  <div class="thumbs">
    <div class="thumb" role="img" aria-label="Thumbnail photo of a customer's pet"></div>
    <div class="thumb" role="img" aria-label="Thumbnail photo of a customer's pet"></div>
    <div class="thumb" role="img" aria-label="Thumbnail photo of a customer's pet"></div>
    <div class="thumb" role="img" aria-label="Thumbnail photo of a customer's pet"></div>
  </div>
</section>
<a class="rewards-pill"><i></i>Summer Vet Rewards</a>
<a class="chat-btn" aria-label="Chat"><svg viewBox="0 0 44 44" width="44" height="44" fill="#fff"><path d="M13 14h18a3 3 0 0 1 3 3v9a3 3 0 0 1-3 3H20l-6 5v-5h-1a3 3 0 0 1-3-3v-9a3 3 0 0 1 3-3z"/></svg></a>

<footer class="site-footer">
  <div class="footer-brand"><i></i>Tumble Tail</div>
  <div class="social"><i></i><i></i><i></i></div>
  <ul class="contact"><li>+1 555 0182</li><li>hello@tumbletail.com</li></ul>
  <ul class="footer-col col-company"><h4>COMPANY</h4><li>Shop</li><li>Our Story</li><li>Blog Plus</li><li>Pet Beauty Kit</li></ul>
  <ul class="footer-col col-help"><h4>HELP &amp; SUPPORT</h4><li>Returns &amp; Exchanges</li><li>FAQ</li><li>Order Support</li><li>Contact</li></ul>
  <div class="newsletter"><h4>SUBSCRIBE TO OUR NEWSLETTER</h4><p>Stay up to date with our latest news and products.</p><div class="news-form"><span>Enter your email</span><b>Subscribe</b></div></div>
</footer>
<div class="footer-bottom">© 2024 Tumble Tail. All rights reserved.</div>

</body>
</html>
```